VENTURE CAPITAL GROUP BUSINESS CARD DESIGN

Venture Capital Group based in SF looking for a bold business card design. No trendy colour explosion, 3D effects etc. Just "simple" optical effects. Works on your brain, keeps your eye focused and sticks to your mind.
Target Market(s)
Technology startups
Industry/Entity Type
Venture Capital
Contact Information for Business Card
BARNABY WHITLOCK
MANAGING PARTNER
817 FERN ST SAN FRANCISCO, CA 94111
415.555.0143 O
415.555.0167 F
415.555.0192 C
barn@halcyonridgefund.example

```html
<!DOCTYPE html>
<html lang="en">
<head>
<meta charset="utf-8">
<title>Halcyon Ridge Capital Group — Business Card</title>
<link href="https://fonts.googleapis.com/css2?family=Cinzel:wght@400;500&family=Arimo:wght@400&display=swap" rel="stylesheet">
<style>
  :root {
    --backdrop: #e6e2da;
    --card-grey: #6f8589;
    --band-green: #0b7a12;
    --band-line: #2f6a33;
    --band-black: #000000;
    --mark-green: #0a5a10;
    --mark-circle: #7f959a;
    --tagline: #10301a;
    --ink: #061206;
  }
  * { box-sizing: border-box; margin: 0; padding: 0; }
  html, body { width: 1200px; height: 1200px; overflow: hidden; }
  body { background: var(--backdrop); position: relative; font-family: "Arimo", Arial, sans-serif; color: var(--ink); }

  .card {
    position: absolute; left: 180px; width: 840px; height: 480px;
    background: var(--card-grey); overflow: hidden;
    box-shadow: 0 6px 14px rgba(0,0,0,.25);
  }
  .card--front { top: 70px; }
  .card--back { top: 650px; }

  .band { position: absolute; left: 0; width: 100%; }
  .band--top { top: 0; height: 12px; background: var(--band-green); }
  .card--back .band--top { height: 40px; }
  .band--info { top: 250px; height: 174px; background: var(--band-green); }
  .band--info::after {
    content: ""; position: absolute; left: 0; right: 0; top: 20px;
    height: 2px; background: var(--band-line);
  }
  .band--bottom { bottom: 0; height: 56px; background: var(--band-black); }
  .card--back .band--bottom { height: 52px; }

  .brand { position: absolute; left: 0; width: 100%; text-align: center; }
  .brand__circle {
    display: block; margin: 0 auto; width: 140px; height: 140px;
    border-radius: 50%; background: var(--mark-circle);
  }
  .brand__name, .brand__sub {
    font-family: "Cinzel", "Times New Roman", serif; font-weight: 400;
    line-height: 1;
  }
  .brand__name { font-size: 40px; margin-top: 22px; letter-spacing: 1px; color: var(--mark-green); }
  .brand__sub { font-size: 12px; letter-spacing: 7px; margin-top: 6px; color: var(--tagline); }
  .card--front .brand { top: 22px; }
  .card--back .brand { top: 110px; }

  .person { position: absolute; top: 284px; left: 0; width: 100%; text-align: center; }
  .person__name { font-size: 20px; }
  .person__title { font-size: 16px; margin-top: 6px; }

  .phones {
    position: absolute; top: 354px; left: 140px; right: 120px;
    display: flex; justify-content: space-between; font-size: 17px;
  }
  .phones span b { font-weight: 400; margin-right: 8px; }

  .contact {
    position: absolute; top: 392px; left: 48px; right: 48px;
    display: flex; justify-content: space-between; align-items: center; font-size: 17px;
  }
  .contact__item { display: flex; align-items: center; gap: 8px; }
  .contact__item svg { width: 18px; height: 18px; fill: var(--ink); }
</style>
</head>
<body>

<section class="card card--front" aria-label="Card front">
  <div class="band band--top"></div>
  <div class="band band--info"></div>
  <div class="band band--bottom"></div>

  <div class="brand">
    <span class="brand__circle"></span>
    <p class="brand__name">HALCYON RIDGE</p>
    <p class="brand__sub">CAPITAL GROUP</p>
  </div>

  <div class="person">
    <p class="person__name">Barnaby Whitlock</p>
    <p class="person__title">Managing Partner</p>
  </div>

  <div class="phones">
    <span><b>[O]</b>415.555.0143</span>
    <span><b>[F]</b>415.555.0167</span>
    <span><b>[C]</b>415.555.0192</span>
  </div>

  <div class="contact">
    <span class="contact__item">
      <svg viewBox="0 0 20 20" aria-hidden="true"><circle cx="10" cy="10" r="9" fill="none" stroke="#061206" stroke-width="2"/><path d="M4 7c3 0 4 2 6 2s2 3 0 4-1 4-2 5C5 17 3 12 4 7z"/></svg>
      barn@halcyonridgefund.example
    </span>
    <span class="contact__item">
      <svg viewBox="0 0 20 20" aria-hidden="true"><path d="M10 1a6 6 0 0 0-6 6c0 5 6 12 6 12s6-7 6-12a6 6 0 0 0-6-6zm0 8.5A2.5 2.5 0 1 1 10 4.5a2.5 2.5 0 0 1 0 5z"/></svg>
      817 Fern St. San Francisco, CA 94111
    </span>
  </div>
</section>

<section class="card card--back" aria-label="Card back">
  <div class="band band--top"></div>
  <div class="band band--bottom"></div>
  <div class="brand">
    <span class="brand__circle"></span>
    <p class="brand__name">HALCYON RIDGE</p>
    <p class="brand__sub">CAPITAL GROUP</p>
  </div>
</section>

</body>
</html>
```